Talent Management Company Needs Business Cards

Using one of the logos provided (attached) K&R Talent Collective needs a business card designed.
Please visit our website for more information about us-

www.krtalentcollective.example

The face should feature a dramatic presentation of the logo with the back being reserved for our professional information which is:

The information should be:
Dorian T. Vickers
C.E.O
Email: dtvickers@krtalentcollective.example
Mobile: 555-804-2917
Website: www.krtalentcollective.example

Marcus L. Vickers
Director of Public Relations
Email: mlvickers@krtalentcollective.example
Mobile: 555-806-3350

Jules R. Hampton
Director of Client Development
Email: jhampton@krtalentcollective.example

Simon Hurlock
Director of Brand Development
Email: shurlock@krtalentcollective.example

Would like the logo to have color. I would like to see one side red or black and the other side white but if it looks better in either black or red that would be fine to but would like to see how it comes out.

Please feel free to message me and if you would like just the icon alone I have other image files that I can send as well.

Target Market(s)

Professional Athletes, coaches, entertainers age 18-35 but also must be accepted in the business community

Industry/Entity Type

Business

Requirements
Must have
• 1) Use the logo
2) Double sided
3) Distinctive
Nice to have
• Small simple images for telephone, e-mail, and Url.

```html
<!DOCTYPE html>
<html lang="en">
<head>
<meta charset="utf-8">
<title>K&amp;R Talent Collective — Business Card</title>
<link rel="stylesheet" href="https://fonts.googleapis.com/css2?family=Questrial&display=swap">
<style>
  :root {
    --stage: #3d3b4d;
    --card: #ffffff;
    --band: #f2f2ee;
    --band-edge: #e2e2dc;
    --accent-red: #e8001c;
    --brand-grey: #5a5a5a;
    --contact: #7a6a6e;
  }
  html, body {
    margin: 0;
    padding: 0;
    width: 1200px;
    height: 885px;
    overflow: hidden;
    background: var(--stage);
  }
  .stage {
    position: relative;
    width: 1200px;
    height: 885px;
    font-family: "Questrial", "Century Gothic", sans-serif;
  }
  .card {
    position: absolute;
    filter: drop-shadow(2px 3px 2px rgba(0,0,0,0.35));
  }
  .card--large { left: 216px; top: 38px; width: 816px; height: 480px; }
  .card--small { left: 410px; top: 560px; width: 459px; height: 270px; }
  .card-face { fill: var(--card); }
  .brand-band { fill: var(--band); }
  .band-edge { stroke: var(--band-edge); stroke-width: 2; }
  .brand-name { fill: var(--brand-grey); font-size: 19px; letter-spacing: 4px; }
  .brand-dot { fill: var(--accent-red); }
  .person-name { fill: var(--accent-red); font-size: 31px; }
  .person-title { fill: var(--accent-red); font-size: 23px; }
  .contact-line { fill: var(--contact); font-size: 16px; letter-spacing: 1px; }
  .contact-line--mobile { letter-spacing: 4px; font-size: 16px; }
  .contact-line--email { font-size: 14px; letter-spacing: 0.5px; }
</style>
</head>
<body>
<main class="stage">
  <svg width="0" height="0" style="position:absolute" aria-hidden="true">
    <defs>
      <symbol id="business-card" viewBox="0 0 816 480">
        <path class="card-face" d="M40,0 L678,0 L816,140 L816,480 L36,480 Q0,480 0,444 L0,40 Q0,0 40,0 Z"/>
        <path class="brand-band" d="M286,0 L678,0 L816,140 L816,480 L754,480 Z"/>
        <line class="band-edge" x1="286" y1="0" x2="754" y2="480"/>

        <circle class="brand-dot" cx="668" cy="122" r="24"/>
        <text class="brand-name" x="462" y="64" transform="rotate(46 462 64)">K &amp; R TALENT COLLECTIVE</text>

        <text class="person-name" x="352" y="190" transform="rotate(46 352 190)">Dorian T. Vickers</text>
        <text class="person-title" x="282" y="168" transform="rotate(46 282 168)">Chief Executive Officer</text>

        <text class="contact-line contact-line--mobile" x="186" y="178" transform="rotate(46 186 178)">Mobile: 555 804 2917</text>
        <text class="contact-line" x="132" y="166" transform="rotate(46 132 166)">www.krtalentcollective.example</text>
        <text class="contact-line contact-line--email" x="74" y="148" transform="rotate(46 74 148)">dtvickers@krtalentcollective.example</text>
      </symbol>
    </defs>
  </svg>

  <svg class="card card--large" viewBox="0 0 816 480" aria-label="Business card, full size">
    <use href="#business-card"/>
  </svg>
  <svg class="card card--small" viewBox="0 0 816 480" aria-label="Business card, actual size">
    <use href="#business-card"/>
  </svg>
</main>
</body>
</html>
```